High End Notary Service Business Card Design

Want a professional and elegant/luxurious business card that is clean and simple in the design. A notary is a trusted professional that helps people sign very important documents. The card should be in alignment with this service provided.

Most of the time, service will be for the purchase of a home or refinance of a mortgage

There is NO LOGO. This is aesthetic. A look and feel. Conveying professionalism and concierge level of service.

Target Market(s)

Other business professionals, Lawyers, Escrow Officers, Loan Officers

Industry/Entity Type

Legal

Contact Information for Business Card

This will be a one-sided business card

Colors
35a7d7
3176b5
85cae6
d3a5cc
b868aa
ffffff
0356a4

Requirements
Must have
• Lorena T. Mirabel-Hodgkins
Notary Public

642-871-3094
MirabelSigningDesk@Wexmail.com
Nice to have
• Headshot photo below. Convey the aspect of signing documents. No black cards. Preference is shades of blue: light blue, navy, aqua, gold, white, or lavendar, etc.
Should not have
• No scales or legal scales.

```html
<!DOCTYPE html>
<html lang="en">
<head>
<meta charset="utf-8">
<title>Lorena T. Mirabel-Hodgkins — Notary Public Business Card</title>
<link rel="stylesheet" href="https://fonts.googleapis.com/css2?family=Mrs+Saint+Delafield&family=Montserrat:ital,wght@0,400;0,500;0,600;1,400&display=swap">
<style>
  :root {
    --page-bg: #ffffff;
    --card-bg: #ffffff;
    --card-border: #4a4a4a;
    --ink: #1c1a1b;
    --ink-soft: #2b2b2b;
    --rule: #2b2b2b;
  }
  * { box-sizing: border-box; margin: 0; padding: 0; }
  html, body {
    width: 1200px;
    height: 1200px;
    overflow: hidden;
    background: var(--page-bg);
  }
  .artboard {
    position: relative;
    width: 1200px;
    height: 1200px;
    font-family: "Montserrat", Arial, sans-serif;
    color: var(--ink);
  }
  .size-label {
    position: absolute;
    left: 248px;
    top: 343px;
    font-size: 22px;
    color: var(--ink-soft);
  }
  .business-card {
    position: absolute;
    left: 248px;
    top: 416px;
    width: 756px;
    height: 433px;
    background: var(--card-bg);
    border: 1.5px solid var(--card-border);
  }
  .signature {
    position: absolute;
    left: 48px;
    top: 30px;
    font-family: "Mrs Saint Delafield", cursive;
    font-size: 200px;
    line-height: 1;
    color: var(--ink);
    white-space: nowrap;
  }
  .holder {
    position: absolute;
    right: 57px;
    top: 296px;
    text-align: right;
  }
  .holder-name {
    font-size: 24px;
    font-weight: 400;
    letter-spacing: 0.3px;
    line-height: 1.2;
  }
  .holder-title {
    margin-top: 6px;
    font-size: 17px;
    font-style: italic;
    line-height: 1.2;
  }
  .divider {
    position: absolute;
    left: 55px;
    right: 57px;
    top: 366px;
    height: 0;
    border-top: 1.5px solid var(--rule);
  }
  .contact-line {
    position: absolute;
    right: 57px;
    top: 386px;
    font-size: 17px;
    font-weight: 500;
    letter-spacing: 1.2px;
    white-space: nowrap;
  }
  .contact-line .separator { margin: 0 12px; }
</style>
</head>
<body>
  <main class="artboard">
    <p class="size-label">Size: 3.5” x 2”</p>
    <section class="business-card">
      <p class="signature">Lorena</p>
      <div class="holder">
        <p class="holder-name">Lorena T. Mirabel-Hodgkins</p>
        <p class="holder-title">Notary Public</p>
      </div>
      <div class="divider"></div>
      <p class="contact-line">
        <span class="phone">642-871-3094</span><span class="separator">|</span><span class="email">MirabelSigningDesk@Wexmail.com</span>
      </p>
    </section>
  </main>
</body>
</html>
```